Bright Ridge Painting and Remodeling New Facebook Design Project

Facebook should include company logo.

Name of company: Bright Ridge Painting and Remodeling
Address: 4612 NW 28th st Suite 519
Miami, FL 33174

local phone: (305) 555-0147
toll free (855) 555-0192
fax (866) 555-0136

email: corla@paintingbrightridge.example

let me know if links to other social media should be included.

company does interior and exterior painting, staining, pressure washing, wall paper removal, tile installation, tile removal, specializing in vinyl floor removal and any of your remodeling needs.

we give free estimates.

Designer can add nice pictures of homes showing painting of interior exterior etc.

Or even videos or whatever they feel is necessary to make an impression to consumers.

Be creative. Page should be professional but eye catching.

Reason: I started getting good designs submitted on the last day want to give designers an opportunity to submit more

Industry/Entity Type

Painting And Decorating

Requirements
Must have
• Professional wording/ font and pictures.
• Creative professional design and colors.
Nice to have
• Pictures of the services offered
• Videos about/and or of the services being offered
Should not have
• N/A

```html
<!DOCTYPE html>
<html lang="en">
<head>
<meta charset="utf-8">
<title>Bright Ridge Painting and Remodeling — Cover Design</title>
<link rel="stylesheet" href="https://fonts.googleapis.com/css2?family=Bitter:ital,wght@0,700;1,800&display=swap">
<style>
  :root {
    --stage: #ebe8e4;
    --paper: #f4f4f2;
    --ink: #1f1f1f;
    --teal: #7fc3bd;
    --lilac: #9c86b8;
    --violet: #6f5a92;
    --leaf: #8cbf74;
    --logo-ink: #3a3a3a;
    --logo-dot: #e59a4a;
  }
  * { margin: 0; padding: 0; box-sizing: border-box; }
  html, body {
    width: 1200px; height: 1000px; overflow: hidden;
    background: var(--stage);
  }
  .cover {
    position: absolute; left: 0; top: 120px;
    width: 1200px; height: 453px;
    overflow: hidden;
    background: var(--paper);
  }
  .cover-photo {
    position: absolute; inset: 0;
    background:
      radial-gradient(ellipse 260px 140px at 110px 40px, var(--leaf) 0%, transparent 80%),
      linear-gradient(160deg, transparent 30%, rgba(127,195,189,.85) 38%, rgba(127,195,189,.85) 52%, transparent 60%),
      linear-gradient(115deg, transparent 62%, rgba(156,134,184,.55) 70%, rgba(111,90,146,.85) 88%, var(--violet) 100%),
      linear-gradient(180deg, #f6f6f4 0%, #e4e4e2 100%);
  }
  .service-list {
    position: absolute; right: 155px; top: 14px;
    list-style: none; text-align: right;
    font-family: "Bitter", Georgia, serif; font-weight: 700;
    font-size: 26px; line-height: 31px; color: var(--ink);
    text-shadow: 2px 2px 3px rgba(0,0,0,.35);
  }
  .service-list li::before { content: "• "; }
  .estimate-line {
    position: absolute; left: 155px; bottom: 4px;
    font-family: "Bitter", Georgia, serif; font-style: italic; font-weight: 800;
    font-size: 32px; letter-spacing: .5px; color: var(--ink);
    text-shadow: 2px 2px 3px rgba(0,0,0,.35);
  }
  .profile-tile {
    position: absolute; left: 40px; top: 620px;
    width: 260px; height: 260px;
    background: #fff; border: 1px solid #d3d3d3;
    display: flex; align-items: center; justify-content: center; gap: 10px;
    padding: 20px;
  }
  .profile-dot {
    flex: none; width: 22px; height: 22px; border-radius: 50%;
    background: var(--logo-dot);
  }
  .profile-name {
    font-family: "Bitter", Georgia, serif; font-weight: 700;
    font-size: 17px; line-height: 21px; color: var(--logo-ink);
  }
</style>
</head>
<body>
  <section class="cover">
    <div class="cover-photo" role="img" aria-label="Photo of fanned paint colour swatches in teal, purple and green with a paint roller on a white surface"></div>
    <ul class="service-list">
      <li>Interior &amp; Exterior Painting</li>
      <li>Staining</li>
      <li>Pressure Washing</li>
      <li>Wall Paper Removal</li>
      <li>Tile Installation &amp; Removal</li>
      <li>Vinyl Floor Removal</li>
      <li>Any of your remodeling needs</li>
    </ul>
    <p class="estimate-line">ALWAYS FREE ESTIMATES</p>
  </section>

  <aside class="profile-tile">
    <span class="profile-dot"></span>
    <span class="profile-name">Bright Ridge Painting and Remodeling</span>
  </aside>
</body>
</html>
```